Business Card and Letterhead for Pemlo - modern real estate business

I need a double sided business card design for Pemlo. Please see business card brief here https://files.quillnote-hub.net/page/7RtxQmZbn4LsWe2VyHoPk9dFjuC3gaXrTmqEi5Ns_pz/view?mode=shared

Please feel free to design the business cards however you feel best. I am happy to give some creative freedoms and then provide feedback from there.

Please then also create a letterhead to match the business card design

Colors

Designer to choose colors to be used in the design.

Requirements
Must have
• Must be a modern, elegant business card which looks very professional

```html
<!DOCTYPE html>
<html lang="en">
<head>
<meta charset="utf-8">
<title>Pemlo Business Card</title>
<link rel="stylesheet" href="https://fonts.googleapis.com/css2?family=Roboto:wght@400;500;700;900&display=swap">
<style>
  :root {
    --brand-red: #e30613;
    --ink-dark: #2a2a2a;
    --ink-muted: #555555;
    --rule-grey: #a8a8a8;
    --card-white: #ffffff;
    --card-charcoal: #2b2b2b;
    --page-bg: #ecebe8;
    --photo-tone: linear-gradient(160deg, #8a9a78 0%, #6b6f64 45%, #2c2c2e 100%);
  }
  * { margin: 0; padding: 0; box-sizing: border-box; }
  html, body {
    width: 1125px;
    height: 1200px;
    overflow: hidden;
  }
  body {
    background: var(--page-bg);
    font-family: "Roboto", Arial, sans-serif;
    position: relative;
  }
  .card {
    position: absolute;
    left: 166px;
    width: 800px;
    height: 456px;
    box-shadow: 0 4px 10px rgba(0,0,0,0.18);
  }
  .card-front { top: 103px; background: var(--card-white); }
  .card-back { top: 620px; background: var(--card-charcoal); }

  .agent-photo {
    position: absolute;
    left: 643px;
    top: 44px;
    width: 106px;
    height: 116px;
    border-radius: 10px;
    border: 2px solid #6a6a6a;
    background: var(--photo-tone);
  }
  .agent-name {
    position: absolute;
    right: 46px;
    top: 178px;
    font-size: 26px;
    font-weight: 700;
    color: var(--brand-red);
    text-align: right;
  }
  .agent-title {
    position: absolute;
    right: 46px;
    top: 210px;
    font-size: 18px;
    font-weight: 500;
    color: var(--ink-dark);
    text-align: right;
  }
  .wordmark {
    font-weight: 900;
    color: var(--brand-red);
    letter-spacing: 0.04em;
    line-height: 1;
  }
  .card-front .wordmark {
    position: absolute;
    left: 48px;
    top: 271px;
    font-size: 64px;
  }
  .divider {
    position: absolute;
    left: 46px;
    top: 350px;
    width: 704px;
    height: 1px;
    background: var(--rule-grey);
  }
  .contact {
    position: absolute;
    font-size: 18px;
    line-height: 23px;
    color: var(--ink-muted);
  }
  .contact-address { left: 49px; top: 377px; }
  .contact-direct { left: 332px; top: 373px; }
  .contact-web { right: 51px; top: 399px; text-align: right; }

  .card-back .wordmark {
    position: absolute;
    left: 0;
    right: 0;
    top: 178px;
    text-align: center;
    font-size: 110px;
  }
</style>
</head>
<body>
  <section class="card card-front">
    <div class="agent-photo" role="img" aria-label="Portrait photo of the agent"></div>
    <h1 class="agent-name">Liam Carver</h1>
    <p class="agent-title">Licenced Real Estate Agent</p>
    <div class="wordmark">PEMLO</div>
    <div class="divider"></div>
    <p class="contact contact-address">PO Box 5120<br>Hillcrest NSW 2780</p>
    <p class="contact contact-direct">P. 0400 318 552<br>E. liam@pemlo.com</p>
    <p class="contact contact-web">www.pemlo.com</p>
  </section>

  <section class="card card-back">
    <div class="wordmark">PEMLO</div>
  </section>
</body>
</html>
```